Presentation Folder and Inserts for Scientific Recruiting Firm

Harborline Staffing is a Pharmaceutical and Biotech recruiting firm. We help companies locate ideal candidates to fill positions within their companies. We want to have presentation materials designed to be handed out to clients at career fairs.

 

WE ARE OPEN TO ALL TYPES OF DESIGNS. 

 

We will have the need for the design of many more projects in the coming months.  We would love to find a great designer to work with on all of our future work.  

 

Part 1: Presentation Folder

A presentation folder designed to contain information about Harborline Staffing and our company’s capabilities. This folder should be very professional and give the feeling that our company is reliable. Abstract designs are fine; incorporating different areas of science would be nice as well. We are open to colors/designs but the logo colors must not be changed.

We are looking for something simple and not too busy.  If you can incorporate the above that is great, but we are looking for a simple design.

 

Part 2: Folder Inserts

In one of the pockets of the folder we would like to have three sheets of paper. The paper will be displayed in a descending fashion so that you are able to see the 1.5 inch header on the top of each paper. (Full sheet in back, sheet trimmed 1.5 inches, sheet trimmed 3 inches in the front. The top 1.5 inch border is all that will need to be designed; we will trim the sheets after printing.

Target Market(s)

Human Resources professionals and hiring managers of biotech, pharmaceutical, and scientific companies

Requirements
Must have
• Folder:

• - Harborline Staffing Logo Must been on white background
• - Company slogan must be on the cover, “Precision in Placement”
• Interior
• - Must include space for a business card to be attached on one of the folder flaps
• - The logo and Slogan should also appear on one of the folder interior pocket flaps

• Please use the attached AI format from the company that will be printing out materials There is an outside and inside printing format.

•  

• Inserts:

• - Inserts must have Harborline Staffing Logo on header
• - Insert must have design on the 1.5 inch of the page (Three Pages)
• - Three Sheets must be labeled, Direct Hire, Temporary Staffing, About Harborline Staffing (This text layer must be left editable in the file delivered version for future revisions)

Nice to have
• Pictures or silhouettes of people
• Something incorporating different scientific themes

• Something incorporating several areas of science. Just a few ideas but there are countless areas of science, (Electronics, Medical, Environmental, Pharmaceutical, Biotech, Chemical, Aerospace, Engineering)
Should not have
• We are open to anything that you can think of.  We want to base an entire series of promotional materials on these designs so we are open minded.

```html
<!DOCTYPE html>
<html lang="en">
<head>
<meta charset="utf-8">
<title>Harborline Staffing – Presentation Folder and Inserts</title>
<link rel="stylesheet" href="https://fonts.googleapis.com/css2?family=Barlow:wght@400;500;600&family=Tinos&display=swap">
<style>
  :root {
    --green: #1d6b37;
    --green-deep: #0f4a26;
    --green-header: #1f5e31;
    --olive: #6b5a1e;
    --gold: #b9862a;
    --ink: #222222;
    --paper: #ffffff;
    --fold: #d6d6d6;
    --ghost: rgba(0, 0, 0, 0.07);
  }
  * { box-sizing: border-box; margin: 0; padding: 0; }
  html, body { width: 1200px; height: 2509px; overflow: hidden; background: var(--paper); }
  body { position: relative; font-family: "Barlow", Arial, sans-serif; color: var(--ink); }

  .caption {
    position: absolute; left: 0; width: 1200px; text-align: center;
    font-size: 15px; font-weight: 500; letter-spacing: 0.5px; color: var(--ink);
  }

  .panel { position: absolute; overflow: hidden; background: var(--paper); }
  .folder { box-shadow: 0 2px 6px rgba(0,0,0,0.18); border: 1px solid #cfcfcf; }

  .photo { position: absolute; }
  .fill-soft { background: linear-gradient(160deg, #f4f4f4, #e2e4e3 60%, #f1f1f1); }

  .ghost-words {
    position: absolute; white-space: nowrap; font-weight: 500;
    font-size: 96px; letter-spacing: 2px; color: var(--ghost); line-height: 1;
  }
  .field-strip {
    position: absolute; white-space: nowrap; font-size: 20px; letter-spacing: 1px;
    color: rgba(255,255,255,0.55); z-index: 3; line-height: 1;
  }
  .web {
    position: absolute; font-size: 17px; font-weight: 600; color: var(--green);
  }
  .lockup {
    position: absolute; width: 440px; text-align: center;
  }
  .wordmark {
    display: block; white-space: nowrap; font-weight: 500; color: var(--green);
    letter-spacing: 1px; line-height: 1;
  }
  .slogan {
    display: block; margin-top: 14px; white-space: nowrap; font-weight: 600; color: var(--green);
    font-size: 17px; letter-spacing: 1px;
  }
  .fold-line { position: absolute; top: 0; height: 313px; left: 503px; width: 1px; background: var(--fold); z-index: 4; }

  .cover { left: 348px; top: 60px; width: 503px; height: 688px; transform: scale(0.875); transform-origin: 50% 0; }
  .outside { left: 99px; top: 850px; width: 1007px; height: 688px; }
  .inside { left: 99px; top: 1700px; width: 1007px; height: 685px; }
  .inside .fold-line { height: 432px; background: none; border-left: 1px dashed #c9c9c9; }
  .inside-collage { left: 0; top: 0; width: 503px; height: 432px;
    background: linear-gradient(135deg, #ebebeb, #cfcfcf 35%, #e6e6e6 60%, #c4c4c4 85%, #e9e9e9); }

  .insert-stack { position: absolute; left: 521px; top: 36px; width: 482px; height: 396px; }
  .sheet { position: absolute; left: 0; width: 482px; overflow: hidden; box-shadow: 0 -1px 3px rgba(0,0,0,0.2); }
  .sheet-header { position: relative; height: 81px; overflow: hidden; }
  .sheet-title {
    position: absolute; left: 28px; top: 30px; font-size: 18px; font-weight: 500;
    letter-spacing: 1px; color: #ffffff; z-index: 2;
  }
  .sheet-mark {
    position: absolute; right: 12px; top: 10px; font-size: 11px; font-weight: 500;
    letter-spacing: 0.5px; color: #ffffff; z-index: 2;
  }
  .sheet-ghost {
    position: absolute; left: 300px; top: 26px; font-size: 64px; font-weight: 500;
    color: rgba(255,255,255,0.07); white-space: nowrap; line-height: 1;
  }
  .sheet-direct { top: 0; height: 396px; background: var(--green-header); }
  .sheet-direct .sheet-header { background: var(--green-header); }
  .sheet-temp { top: 81px; height: 315px; background: var(--olive); }
  .sheet-temp .sheet-header { background: linear-gradient(180deg, #76642a, var(--olive)); }
  .sheet-about { top: 162px; height: 234px; background: var(--paper); }
  .sheet-about .sheet-header { background: linear-gradient(180deg, #c4923a, var(--gold)); }
  .sheet-body {
    padding: 10px 24px 0 22px; font-family: "Tinos", "Times New Roman", serif;
    font-size: 9.5px; line-height: 12px; color: #333;
  }
  .sheet-body p { margin-bottom: 7px; }

  .pocket {
    position: absolute; left: 0; top: 432px; width: 1007px; height: 253px; z-index: 5;
    background: linear-gradient(180deg, #236f3d, var(--green-deep));
    overflow: hidden;
  }
  .pocket .ghost-words { top: 20px; left: -20px; color: rgba(255,255,255,0.06); }
  .pocket .field-strip { top: 116px; left: 0; color: rgba(255,255,255,0.08); }
  .pocket-slit { position: absolute; left: 0; top: 0; z-index: 6; }

  .card {
    position: absolute; top: 43px; width: 195px; height: 116px; background: var(--paper); z-index: 7;
    clip-path: polygon(10px 0, 185px 0, 195px 10px, 195px 106px, 185px 116px, 10px 116px, 0 106px, 0 10px);
  }
  .card-band { height: 40px; background: linear-gradient(180deg, #e6e6e6, #cfcfcf); position: relative; }
  .card-band .wordmark { position: absolute; left: 16px; top: 15px; font-size: 13px; }
  .card-info { padding: 6px 16px; font-size: 7.5px; line-height: 10px; color: var(--green); font-weight: 600; }
  .card-info .email { color: var(--gold); font-weight: 500; }
  .card-info .addr { margin-top: 6px; }
  .card-left { left: 160px; }
  .card-right { left: 655px; }
</style>
</head>
<body>

  <section class="panel folder cover" aria-label="Folder front cover">
    <div class="photo fill-soft" style="left:0;top:0;width:503px;height:313px" role="img" aria-label="Faint grey laboratory photo texture"></div>
    <div class="ghost-words" style="left:-30px;top:222px">BIOTECHNOLOGY</div>
    <div class="field-strip" style="left:0;top:318px">ENGINEERING PHARMACEUTICAL ELECTRONICS</div>
    <div class="lockup" style="left:32px;top:150px">
      <span class="wordmark" style="font-size:38px">HARBORLINE STAFFING</span>
      <span class="slogan">PRECISION IN PLACEMENT</span>
    </div>
    <div class="photo" style="left:0;top:313px;width:104px;height:139px;background:#8fbf3a" role="img" aria-label="Lime green glassware photo"></div>
    <div class="photo" style="left:104px;top:313px;width:145px;height:242px;background:linear-gradient(160deg,#b9b2a4,#7d8a8c)" role="img" aria-label="Scientist with pipette photo"></div>
    <div class="photo" style="left:249px;top:313px;width:158px;height:139px;background:#3f8a4c" role="img" aria-label="Green circuit board photo"></div>
    <div class="photo" style="left:407px;top:313px;width:96px;height:242px;background:#8a1e1e" role="img" aria-label="Dark red cells photo"></div>
    <div class="photo" style="left:0;top:452px;width:104px;height:236px;background:linear-gradient(180deg,#4f7fa8,#c46a2a)" role="img" aria-label="Industrial machinery photo"></div>
    <div class="photo" style="left:104px;top:555px;width:145px;height:133px;background:#3da6a0" role="img" aria-label="Teal gloved hands photo"></div>
    <div class="photo" style="left:249px;top:452px;width:158px;height:236px;background:linear-gradient(170deg,#e3e6e2,#cfd6d2)" role="img" aria-label="Measuring beaker scale photo"></div>
    <div class="photo" style="left:407px;top:555px;width:96px;height:133px;background:#b84a3c" role="img" aria-label="Red measuring mark photo"></div>
  </section>
  <p class="caption" style="top:754px">Folder render when folded at center</p>

  <section class="panel folder outside" aria-label="Outside folder spread">
    <div class="photo fill-soft" style="left:0;top:0;width:1007px;height:313px" role="img" aria-label="Faint grey laboratory photo texture"></div>
    <div class="ghost-words" style="left:-10px;top:222px">CHEMISTRY BIOTECHNOLOGY</div>
    <div class="field-strip" style="left:0;top:318px">SPACE CHEMISTRY BIOTECHNOLOGY ENGINEERING PHARMACEUTICAL ELECTRONICS</div>
    <div class="fold-line"></div>
    <div class="web" style="left:162px;top:158px">www.harborlinestaffing.net</div>
    <div class="lockup" style="left:535px;top:150px">
      <span class="wordmark" style="font-size:38px">HARBORLINE STAFFING</span>
      <span class="slogan">PRECISION IN PLACEMENT</span>
    </div>

    <div class="photo" style="left:0;top:313px;width:252px;height:139px;background:linear-gradient(135deg,#3a2a18,#a8742e)" role="img" aria-label="Sparks in workshop photo"></div>
    <div class="photo" style="left:252px;top:313px;width:204px;height:139px;background:#2f7d78" role="img" aria-label="Pipette and dish photo"></div>
    <div class="photo" style="left:456px;top:313px;width:151px;height:139px;background:#8fbf3a" role="img" aria-label="Lime green glassware photo"></div>
    <div class="photo" style="left:607px;top:313px;width:145px;height:242px;background:linear-gradient(160deg,#b9b2a4,#7d8a8c)" role="img" aria-label="Scientist with pipette photo"></div>
    <div class="photo" style="left:752px;top:313px;width:158px;height:139px;background:#3f8a4c" role="img" aria-label="Green circuit board photo"></div>
    <div class="photo" style="left:910px;top:313px;width:97px;height:242px;background:#8a1e1e" role="img" aria-label="Dark red cells photo"></div>
    <div class="photo" style="left:0;top:452px;width:200px;height:236px;background:linear-gradient(160deg,#d9d9d6,#8f948f)" role="img" aria-label="Researcher at bench photo"></div>
    <div class="photo" style="left:200px;top:452px;width:203px;height:100px;background:#5f9a3a" role="img" aria-label="Circuit board components photo"></div>
    <div class="photo" style="left:200px;top:552px;width:203px;height:136px;background:linear-gradient(180deg,#3b9a4a,#7fb7c8)" role="img" aria-label="Rows of sample tubes photo"></div>
    <div class="photo" style="left:403px;top:452px;width:204px;height:236px;background:linear-gradient(180deg,#4f7fa8,#c46a2a)" role="img" aria-label="Industrial machinery photo"></div>
    <div class="photo" style="left:607px;top:555px;width:145px;height:133px;background:#3da6a0" role="img" aria-label="Teal gloved hands photo"></div>
    <div class="photo" style="left:752px;top:452px;width:158px;height:236px;background:linear-gradient(170deg,#e3e6e2,#cfd6d2)" role="img" aria-label="Measuring beaker scale photo"></div>
    <div class="photo" style="left:910px;top:555px;width:97px;height:133px;background:#b84a3c" role="img" aria-label="Red measuring mark photo"></div>
  </section>
  <p class="caption" style="top:1578px">Outside Folder</p>

  <section class="panel folder inside" aria-label="Inside folder spread with inserts and business cards">
    <div class="photo inside-collage" role="img" aria-label="Grey toned collage of laboratory and engineering photos"></div>
    <div class="fold-line"></div>
    <div class="web" style="left:162px;top:287px">www.harborlinestaffing.net</div>

    <div class="insert-stack">
      <div class="sheet sheet-direct">
        <div class="sheet-header">
          <span class="sheet-ghost">DIRECT</span>
          <span class="sheet-title">DIRECT HIRE</span>
          <span class="sheet-mark">HARBORLINE STAFFING</span>
        </div>
      </div>
      <div class="sheet sheet-temp">
        <div class="sheet-header">
          <span class="sheet-ghost">TEMPORARY</span>
          <span class="sheet-title">TEMPORARY STAFFING</span>
          <span class="sheet-mark">HARBORLINE STAFFING</span>
        </div>
      </div>
      <div class="sheet sheet-about">
        <div class="sheet-header">
          <span class="sheet-ghost">ABOUT</span>
          <span class="sheet-title">ABOUT HARBORLINE STAFFING</span>
          <span class="sheet-mark">HARBORLINE STAFFING</span>
        </div>
        <div class="sheet-body">
          <p>Harborline Staffing connects science employers with skilled talent across biotech, pharmaceutical and engineering fields. We screen every candidate for technical depth and lab experience, so hiring managers meet people ready to contribute.</p>
          <p>Our recruiters hold degrees in chemistry, biology and physics. They speak the language of your team and understand the instruments, methods and rules that shape each role.</p>
          <p>From a single contract chemist to a full validation team, we build searches around your timeline. Direct hire and temporary staffing plans can be combined as projects grow, shift or close, and we stay in touch after every placement to make sure it works.</p>
          <p>Call us today to learn how a tailored search can move your next program forward.</p>
        </div>
      </div>
    </div>

    <div class="pocket">
      <div class="ghost-words">CHEMISTRY BIOTECHNOLOGY</div>
      <div class="field-strip">SPACE CHEMISTRY BIOTECHNOLOGY ENGINEERING PHARMACEUTICAL ELECTRONICS</div>
      <svg class="pocket-slit" width="1007" height="253" viewBox="0 0 1007 253" aria-hidden="true">
        <polygon points="486,0 520,0 504,218" fill="#ffffff"/>
      </svg>

      <div class="card card-left">
        <div class="card-band"><span class="wordmark">HARBORLINE STAFFING</span></div>
        <div class="card-info">
          <div>Dana Whitlow <span class="email">dana@harborlinestaffing.net</span></div>
          <div>1.503.555.0148</div>
          <div class="addr">410 Foundry Lane</div>
          <div>Portland, OR 97209</div>
        </div>
      </div>
      <div class="card card-right">
        <div class="card-band"><span class="wordmark">HARBORLINE STAFFING</span></div>
        <div class="card-info">
          <div>Dana Whitlow <span class="email">dana@harborlinestaffing.net</span></div>
          <div>1.503.555.0148</div>
          <div class="addr">410 Foundry Lane</div>
          <div>Portland, OR 97209</div>
        </div>
      </div>
    </div>
  </section>
  <p class="caption" style="top:2424px">Inside Folder with Business Cards and Inserts</p>

</body>
</html>
```